Lumen Keyvault Password Manager WebApp Design

Lumen Keyvault is seeking an expert UI designer to provide a fresh and modern visual appeal for our product. Our inspiration comes from two major tools that have successfully managed to balance functionality and design aesthetics - Orbix Folder and Vaultmint. We want our application to exude a similar trustworthiness and modernity, through a clean, intuitive and responsive design.
We have established preliminary mockups and would like the designer to work within these parameters while enhancing the overall user experience. The primary tasks will involve innovative and improved designs of the login screen and the password screen, both being crucial touchpoints for our users. The login screen also serves a crucial role in demonstrating how our system works.
Key Elements:
Logo Integration: We are providing the logo for Lumen Keyvault. The design should align with the logo, both in terms of colors and overall aesthetic, to ensure a cohesive brand identity.
Color Palette: The UI design should adhere to the color palette derived from the logo to maintain brand consistency. The design should effectively utilize these colors to highlight important elements and improve user engagement.
Trustworthy and Modern Design: The UI should be professional and trustworthy. It should mirror the look and feel of Orbix Folder's simplicity and Vaultmint's solid security design, which inspires user confidence.
Adherence to Mockup Boundaries: The existing mockups serve as a guideline for the layout and placement of elements. The design should respect these boundaries while bringing innovation and visual appeal.
Improved Login Screen: The login screen is a key part of the user's journey and should be designed with utmost care. It should be intuitive, easy-to-use, visually engaging, and educative, showcasing how the system operates and encouraging users to sign in with confidence.
Enhanced Password Screen: The password screen, another key user touchpoint, needs improvement. The different types of passwords should be made more visible and intuitive, easing user interaction and enhancing the overall experience.
Prospective designers are encouraged to test our current version available for free at app.lumenkeyvault.com to understand the product better and contribute to meaningful design enhancements.
The goal of this project is to provide a visually compelling and user-friendly interface for Lumen Keyvault that inspires user trust, while adhering to the branding elements, including color scheme and logo design. The ideal designer will have a proven track record of creating compelling UI designs that enhance user experience and engagement.
We preferred the design to be in Figma.
Please provide the 3 design so we can evaluate if we like to choice you:
1. Login Page.
2. Passwords View design
3. Single Passwod Page
We need all the pages to be design that are provided as screenshots.

```html
<!DOCTYPE html>
<html lang="en">
<head>
<meta charset="utf-8">
<title>Lumen Keyvault – Login</title>
<link href="https://fonts.googleapis.com/css2?family=Inter:wght@400;500;600;700;800&display=swap" rel="stylesheet">
<style>
:root{
  --ink:#0f1426;
  --text:#1d2233;
  --muted:#4a5163;
  --blue:#3370d9;
  --blue-dark:#2453b3;
  --navy:#2f2d6b;
  --red:#e23b3b;
  --pink:#fcd7d7;
  --white:#ffffff;
  --green:#27a36a;
}
*{box-sizing:border-box;margin:0;padding:0}
html,body{width:1200px;height:702px;overflow:hidden}
body{
  position:relative;font-family:"Inter",sans-serif;color:var(--text);
  background:
    radial-gradient(circle at 18% 82%, #b7949c 0, rgba(183,148,156,0) 32%),
    radial-gradient(circle at 35% 20%, #8fa6ac 0, rgba(143,166,172,0) 40%),
    linear-gradient(160deg,#a3adbf 0%,#97a4b6 45%,#a4aabf 100%);
}
.abs{position:absolute}
.brand{left:33px;top:20px;display:flex;align-items:center;gap:8px;font-size:15px;color:#3a4254}
.brand-mark{width:24px;height:24px;border-radius:4px;background:var(--blue-dark)}
.nav{top:30px;font-size:12.5px;color:var(--ink)}
.nav-btn{left:1033px;top:17px;width:133px;height:27px;border:1px solid var(--blue);border-radius:14px;color:var(--blue);font-size:12.5px;display:flex;align-items:center;justify-content:center}
.pill{left:32px;top:129px;width:261px;height:32px;border-radius:16px;background:rgba(255,255,255,.18);display:flex;align-items:center;gap:10px;padding-left:18px;font-size:14px;color:var(--ink)}
.headline{left:33px;top:172px;font-size:54px;line-height:62px;font-weight:800;color:var(--ink);letter-spacing:-1px;white-space:nowrap}
.lead{left:33px;top:308px;font-size:17px;line-height:20px;color:#1f2536;white-space:nowrap}
.cta{left:33px;top:382px;width:224px;height:61px;border-radius:12px;background:var(--blue-dark);display:flex;align-items:center;gap:14px;padding-left:14px;color:#dbe5fb;font-size:15px}
.cta-dot{width:35px;height:35px;border-radius:50%;background:#e9ecf2}
.card{background:rgba(255,255,255,.1);border-radius:14px}
.card-title{font-weight:700;font-size:15px;color:#2b2c5e}
.bar{height:4px;border-radius:2px;background:rgba(255,255,255,.35)}
.bar span{display:block;height:100%;border-radius:2px}
.card-note{font-size:12px;color:#555d70}
.plus{left:1003px;top:383px;width:36px;height:36px;border-radius:50%;background:var(--navy);color:#fff;font-size:22px;display:flex;align-items:center;justify-content:center}
.features .feat{position:absolute;top:546px;display:flex;gap:8px}
.tick{width:48px;height:48px;border-radius:50%;background:rgba(255,255,255,.1);border:1px solid rgba(255,255,255,.2);display:flex;align-items:center;justify-content:center;flex:none}
.feat h3{font-size:12.5px;font-weight:700;color:var(--ink);margin:2px 0 4px 2px}
.feat p{font-size:12px;line-height:14px;color:#222839}
.footer{left:33px;top:676px;font-size:10.5px;color:#4c5366}
.footer a{color:var(--blue-dark)}
.modal{left:367px;top:107px;width:465px;height:391px;background:var(--white);border-radius:20px;overflow:hidden}
.close{right:24px;top:24px}
.lock-badge{left:212px;top:47px;width:42px;height:42px;border-radius:50%;background:var(--blue);display:flex;align-items:center;justify-content:center}
.greet{top:103px;width:100%;text-align:center;font-size:27px;font-weight:800;color:var(--ink)}
.hint{top:136px;width:100%;text-align:center;font-size:11.5px;color:#4e5566}
.label{left:115px;top:167px;font-size:11px;color:var(--ink)}
.field{left:115px;top:182px;width:236px;height:40px;border:1px solid var(--red);border-radius:8px;display:flex;align-items:center;padding:0 12px;gap:10px}
.dots{flex:1;font-size:14px;letter-spacing:1px;color:var(--ink)}
.error{left:115px;top:227px;width:236px;height:24px;border-radius:6px;background:var(--pink);display:flex;align-items:center;gap:6px;padding-left:8px;font-size:10.5px;color:#b3202a}
.login{left:115px;top:269px;width:236px;height:40px;border-radius:8px;background:var(--blue);color:#fff;font-size:12.5px;display:flex;align-items:center;justify-content:center}
.divider{left:0;top:339px;width:100%;height:1px;background:#e2e4ea}
.help{top:360px;width:100%;text-align:center;font-size:10.5px;color:var(--blue)}
.help a{color:inherit}
</style>
</head>
<body>
<header>
  <div class="abs brand"><span class="brand-mark"></span>Lumen Keyvault</div>
  <div class="abs nav" style="left:786px">Back to Website</div>
  <div class="abs nav" style="left:922px">How it works?</div>
  <div class="abs nav-btn">Sign in with Orbix</div>
</header>

<section class="hero">
  <div class="abs pill">
    <svg width="11" height="13" viewBox="0 0 11 13"><rect x="0.5" y="5" width="10" height="7.5" rx="1.5" fill="#7d8070"/><path d="M2.5 5V3.5a3 3 0 0 1 6 0V5" fill="none" stroke="#7d8070" stroke-width="1.3"/></svg>
    Securely protect your passwords
  </div>
  <h1 class="abs headline">Simplify and Secure<br>Your Digital Life</h1>
  <p class="abs lead">Safeguard your sensitive data with password-protected<br>secure storage within your Orbix Folder</p>
  <div class="abs cta"><span class="cta-dot"></span>Sign in with Orbix</div>
</section>

<aside class="showcase">
  <div class="abs" style="left:1057px;top:117px;width:26px;height:26px;border-radius:50%;background:#3d5fa8;filter:blur(2px)"></div>
  <div class="abs card" style="left:835px;top:155px;width:147px;height:217px">
    <div class="abs" style="left:30px;top:45px;width:34px;height:34px;border-radius:50%;background:rgba(255,255,255,.3)"></div>
    <div class="abs" style="left:122px;top:12px;width:9px;height:9px;border-radius:50%;background:#b54a52"></div>
    <div class="abs card-title" style="left:18px;top:118px">Orbix Folder</div>
    <div class="abs bar" style="left:19px;top:157px;width:105px"><span style="width:45%;background:var(--green)"></span></div>
    <div class="abs card-note" style="left:17px;top:173px">Linked your account</div>
  </div>
  <div class="abs card" style="left:1005px;top:205px;width:55px;height:55px;display:flex;align-items:center;justify-content:center">
    <svg width="22" height="22" viewBox="0 0 24 24" fill="none" stroke="#5a55d6" stroke-width="2.4" stroke-linecap="round"><path d="M10 14a4 4 0 0 0 5.6 0l3-3a4 4 0 0 0-5.6-5.6l-1 1"/><path d="M14 10a4 4 0 0 0-5.6 0l-3 3a4 4 0 0 0 5.6 5.6l1-1"/></svg>
  </div>
  <div class="abs card-title" style="left:1012px;top:292px">Cloudtrove</div>
  <div class="abs bar" style="left:1012px;top:332px;width:105px"><span style="width:57%;background:#2b5fd0"></span></div>
  <div class="abs card-note" style="left:1011px;top:345px">2 accounts linked</div>
  <div class="abs card" style="left:830px;top:386px;width:152px;height:59px">
    <div class="abs" style="left:-2px;top:14px;font-size:12px;font-weight:600;color:#2b2c5e">Wifi Passwords</div>
    <div class="abs card-note" style="left:5px;top:29px">Wifi passwords</div>
    <div class="abs" style="left:118px;top:16px;font-size:8px;color:#555d70">3:44</div>
    <div class="abs" style="left:107px;top:45px;width:9px;height:9px;border-radius:50%;background:#b54a52"></div>
  </div>
  <div class="abs plus">+</div>
  <div class="abs" style="left:1109px;top:429px;width:14px;height:14px;border-radius:50%;background:#b8935a;filter:blur(1px)"></div>
</aside>

<section class="features">
  <div class="feat" style="left:142px">
    <div class="tick"><svg width="20" height="16" viewBox="0 0 20 16"><path d="M2 8l6 6L18 2" fill="none" stroke="#111" stroke-width="3"/></svg></div>
    <div><h3>No Access required</h3><p>Only you from your browser<br>can connect to your Orbix Folder.</p></div>
  </div>
  <div class="feat" style="left:429px">
    <div class="tick"><svg width="20" height="16" viewBox="0 0 20 16"><path d="M2 8l6 6L18 2" fill="none" stroke="#111" stroke-width="3"/></svg></div>
    <div><h3>Encryption/Decryption Keys</h3><p>Files encrypted with unique keys,<br>aggregated in your browser.</p></div>
  </div>
  <div class="feat" style="left:716px">
    <div class="tick"><svg width="20" height="16" viewBox="0 0 20 16"><path d="M2 8l6 6L18 2" fill="none" stroke="#111" stroke-width="3"/></svg></div>
    <div><h3>We do not store anything</h3><p>Your passwords are stored only on<br>one place - your Orbix Folder™.</p></div>
  </div>
</section>

<footer class="abs footer">By clicking Sign In with Orbix, you agree with our <a href="#">Terms of Use</a>. Learn what data we collect and how we handle it in our <a href="#">Privacy Policy</a></footer>

<div class="abs modal" role="dialog" aria-label="Vault login">
  <svg class="abs close" width="20" height="20" viewBox="0 0 20 20"><path d="M1 1l18 18M19 1L1 19" stroke="#111" stroke-width="2"/></svg>
  <div class="abs lock-badge">
    <svg width="16" height="19" viewBox="0 0 16 19"><path d="M4 8V5a4 4 0 0 1 8 0v3" fill="none" stroke="#cfe0ff" stroke-width="1.8"/><rect x="1" y="8" width="14" height="10" rx="2" fill="#dbe7ff"/><rect x="7.2" y="11" width="1.6" height="4" rx=".8" fill="#3370d9"/></svg>
  </div>
  <h2 class="abs greet">Hi, Milo</h2>
  <p class="abs hint">Authentication is required to access your vault.</p>
  <label class="abs label">Password</label>
  <div class="abs field">
    <svg width="13" height="15" viewBox="0 0 13 15"><path d="M3.5 6V4a3 3 0 0 1 6 0v2" fill="none" stroke="#e23b3b" stroke-width="1.3"/><rect x="1" y="6" width="11" height="8.3" rx="1.5" fill="none" stroke="#e23b3b" stroke-width="1.3"/><path d="M6.5 9v2.5" stroke="#e23b3b" stroke-width="1.3"/></svg>
    <span class="dots">••••••••••••••</span>
    <svg width="15" height="13" viewBox="0 0 24 20" fill="none" stroke="#111" stroke-width="2"><path d="M1 10s4-7 11-7 11 7 11 7-4 7-11 7S1 10 1 10z"/><circle cx="12" cy="10" r="3"/><path d="M3 19L21 1"/></svg>
  </div>
  <div class="abs error">
    <svg width="12" height="12" viewBox="0 0 12 12"><circle cx="6" cy="6" r="6" fill="#e23b3b"/><path d="M6 2.8v4" stroke="#fff" stroke-width="1.4"/><circle cx="6" cy="8.8" r=".8" fill="#fff"/></svg>
    Wrong password. Please try again
  </div>
  <div class="abs login">Login</div>
  <div class="abs divider"></div>
  <p class="abs help"><a href="#">Need help?</a></p>
</div>
</body>
</html>
```